Flyer / Mailer for Business Debt Relief Business - Tillbrook Partners 6" x 11"

We need a 6" x 11" double sided flyer. This will be sent out to potential customers with high interest business loans. We would like the design to coordinate with the colors of our logo. I have included a mock up that we sketched out. I have also included a file of a mailer we received that we would like to use as a template (not colors or fonts, just set up). I have also included an .ai file of our logo.

```html
<!DOCTYPE html>
<html lang="en">
<head>
<meta charset="utf-8">
<title>Tillbrook Partners – Business Debt Relief Mailer</title>
<link rel="stylesheet" href="https://fonts.googleapis.com/css2?family=Bangers&family=Exo+2:ital,wght@1,300&family=Mulish:ital,wght@0,400;0,600;0,800;1,400&family=Raleway:wght@400&display=swap">
<style>
  :root{
    --page:#eef1f4;
    --ink:#111111;
    --text:#333333;
    --blue:#226199;
    --green:#7ab841;
    --lavender:#e4d5e5;
    --white:#ffffff;
    --photo-warm:#b79a78;
    --photo-grey:#c9c8c4;
    --photo-wood:#6b4a33;
    --photo-leaf:#a8b860;
    --photo-shirt:#c7d3e2;
  }
  *{box-sizing:border-box;margin:0;padding:0}
  html,body{width:1200px;height:1200px;overflow:hidden;background:var(--page)}
  body{position:relative;font-family:'Mulish',sans-serif;color:var(--text)}
  .card{position:absolute;left:77px;width:1046px;height:541px;background:var(--white);overflow:hidden}
  .card--front{top:58px}
  .card--back{top:628px}
  .abs{position:absolute}

  /* front: photo column */
  .photo-column{left:0;top:0;width:218px;height:541px;display:flex;flex-direction:column}
  .photo{flex:1}
  .photo--coins{background:linear-gradient(160deg,#e9e6e0,var(--photo-warm))}
  .photo--calculator{background:linear-gradient(160deg,#f1f0ec,var(--photo-grey))}
  .photo--desk{background:linear-gradient(160deg,#8a6446,var(--photo-wood))}
  .photo--growth{background:linear-gradient(160deg,#dfe5a0,var(--photo-leaf))}

  .headline{left:218px;width:610px;top:48px;text-align:center;font-family:'Bangers',sans-serif;font-size:36px;letter-spacing:3.5px;line-height:34px;color:var(--ink);font-style:italic;font-weight:400}

  .brand{display:flex;align-items:center;gap:8px;font-family:'Raleway',sans-serif;color:#444;white-space:nowrap}
  .brand__square{width:13px;height:13px;background:var(--green);flex:none}
  .brand--front{left:800px;width:236px;top:92px;justify-content:center;font-size:13.5px;letter-spacing:1.5px}

  .band-blue{left:218px;top:130px;width:828px;height:80px;background:var(--blue)}
  .band-blue__text{left:218px;width:640px;top:138px;text-align:center;font-family:'Exo 2',sans-serif;font-style:italic;font-weight:300;font-size:25.5px;line-height:34px;color:var(--white);z-index:2}
  .band-green{left:218px;top:210px;width:828px;height:218px;background:var(--green)}
  .band-green__title{left:243px;top:226px;font-family:'Bangers',sans-serif;font-style:italic;font-weight:400;font-size:30px;letter-spacing:1.5px;line-height:31px;color:var(--white);z-index:2}
  .benefits{list-style:none;color:var(--white);font-size:12.5px;line-height:19.2px;z-index:2}
  .benefits li::before{content:"➤ ";font-size:9px}
  .benefits--left{left:246px;top:308px}
  .benefits--right{left:555px;top:307px}
  .portrait{left:872px;top:138px;width:174px;height:290px;background:linear-gradient(180deg,#a9bfd6,var(--photo-shirt));z-index:1}

  .band-contact{left:218px;top:428px;width:828px;height:113px;background:var(--lavender)}
  .contact-web{left:218px;width:315px;top:438px;text-align:center;color:var(--ink)}
  .contact-web__label{font-size:21px;font-weight:600}
  .contact-web__url{font-size:21px;color:var(--blue);margin-top:1px}
  .contact-web__email{font-size:15px;margin-top:5px}
  .contact-divider{left:546px;top:446px;width:2px;height:68px;background:var(--blue)}
  .contact-call{left:560px;width:470px;top:438px;text-align:center;color:var(--ink)}
  .contact-call__label{font-size:18.5px;font-weight:600}
  .contact-call__phone{display:flex;justify-content:center;align-items:center;gap:12px;margin-top:4px;font-size:36px;font-weight:800;color:var(--blue)}

  /* back */
  .brand--back{left:40px;width:240px;top:112px;justify-content:center;font-size:17px;letter-spacing:2px}
  .address{left:40px;width:240px;top:156px;text-align:center;font-size:12.5px;line-height:16px;color:#555}
  .back-title{left:50px;width:290px;top:234px;text-align:center;font-family:'Bangers',sans-serif;font-style:italic;font-weight:400;font-size:20px;letter-spacing:3px;line-height:20px;color:#3a3a3a}
  .back-copy{left:55px;top:300px;font-style:italic;font-size:15.5px;letter-spacing:2px;line-height:20px;color:#333}
</style>
</head>
<body>

<section class="card card--front">
  <div class="abs photo-column">
    <div class="photo photo--coins" role="img" aria-label="Stacked coins with pens on paperwork"></div>
    <div class="photo photo--calculator" role="img" aria-label="Coins, caliper and calculator on financial sheets"></div>
    <div class="photo photo--desk" role="img" aria-label="Desk with laptop and a finance sketch on paper"></div>
    <div class="photo photo--growth" role="img" aria-label="Seedlings growing from coin stacks beside a jar of coins"></div>
  </div>

  <h1 class="abs headline">Helping businesses focus<br>on what metters!</h1>

  <div class="abs brand brand--front"><span class="brand__square"></span>TILLBROOK PARTNERS</div>

  <div class="abs band-blue"></div>
  <div class="abs band-green"></div>
  <div class="abs portrait" role="img" aria-label="Smiling businessman in shirt and tie holding a tablet"></div>

  <p class="abs band-blue__text">We understand that merchant cash advance<br>loans can be a burden on your business</p>

  <h2 class="abs band-green__title">Over whelmed by daily/weekly payments?<br>We can help!</h2>
  <ul class="abs benefits benefits--left">
    <li>This is not a loan, WE ARE NOT LENDERS!</li>
    <li>Improve your business cash flow immediately</li>
    <li>Move payments to one monthly amount</li>
    <li>Reduce the amount you are paying out monthly</li>
    <li>Strategic alternatives to high interest loans</li>
  </ul>
  <ul class="abs benefits benefits--right">
    <li>Fast, confidential business debt relief</li>
    <li>No obligation consultation</li>
    <li>Absolutely no credit pulls</li>
    <li>No collateral, no financia's</li>
  </ul>

  <div class="abs band-contact"></div>
  <div class="abs contact-web">
    <p class="contact-web__label">Visit our website:</p>
    <p class="contact-web__url">www.tillbrookrelief.com</p>
    <p class="contact-web__email">email: info@tillbrookrelief.com</p>
  </div>
  <div class="abs contact-divider"></div>
  <div class="abs contact-call">
    <p class="contact-call__label">Call now for free consultation with our experts</p>
    <p class="contact-call__phone">
      <svg width="40" height="36" viewBox="0 0 40 36" aria-hidden="true">
        <path d="M6 3c2-1 4 0 5 2l3 6c1 2 0 3-1 4l-2 2c2 4 5 7 9 9l2-2c1-1 3-2 4-1l6 3c2 1 3 3 2 5l-2 3c-1 2-4 2-6 1C14 31 6 22 3 10 2 7 3 5 6 3z" fill="var(--blue)"/>
        <path d="M24 4a10 10 0 0 1 10 10M24 10a4 4 0 0 1 4 4" stroke="var(--blue)" stroke-width="2.5" fill="none" stroke-linecap="round"/>
      </svg>
      844-555-0182
    </p>
  </div>
</section>

<section class="card card--back">
  <div class="abs brand brand--back"><span class="brand__square"></span>TILLBROOK PARTNERS</div>
  <p class="abs address">1450 Harrow Ridge Rd<br>Millbrook, Cedar County 76110</p>
  <h2 class="abs back-title">Strategic debt relief for<br>businesses of all sizies</h2>
  <p class="abs back-copy">Stop taking out loans to pay off<br>other loans.<br>Take back your business’s cash<br>flow, and focus on what matters.</p>
</section>

</body>
</html>
```